Stationery Design Project

We are looking for a full revision of our existing stationary to include within this project:

- Letterhead
- Business card
- Compliment slip

The items should be a reflection of our new website which can be found at http://www.larkfieldchecks.co.uk/

Our logo files are included within the file brief

There are some further projects which we may approach the winning designer for as we need a revision to the front cover of our reports, a new price list and two brochures for specific target markets.

Industry/Entity Type

Business

```html
<!DOCTYPE html>
<html lang="en">
<head>
<meta charset="utf-8">
<title>Larkfield Checks — Stationery</title>
<link href="https://fonts.googleapis.com/css2?family=Open+Sans:wght@400;600&family=Noto+Sans:wght@400&display=swap" rel="stylesheet">
<style>
  :root {
    --backdrop: #1b1b1d;
    --paper: #ffffff;
    --brand-navy: #2a2f86;
    --brand-blue: #2f6db2;
    --brand-deep: #2a3f99;
    --ink: #3a3a3a;
    --muted: #8a8a8a;
    --card-glow: #2aa0e6;
  }
  * { margin: 0; padding: 0; box-sizing: border-box; }
  html, body { width: 1200px; height: 900px; overflow: hidden; }
  body {
    background: var(--backdrop);
    font-family: "Open Sans", Arial, sans-serif;
    position: relative;
  }
  .sheet { position: absolute; background: var(--paper); overflow: hidden; }

  .wordmark {
    display: flex; align-items: center; gap: 6px;
    color: var(--brand-navy); font-weight: 600; letter-spacing: 0.2px;
    white-space: nowrap;
  }
  .wordmark .mark-dot { width: 8px; height: 8px; background: currentColor; border-radius: 50%; }

  .wave { position: absolute; left: 0; bottom: 0; width: 100%; display: block; }

  /* Letterhead */
  .letterhead { left: 64px; top: 46px; width: 612px; height: 791px; }
  .letterhead .wordmark { position: absolute; left: 36px; top: 62px; font-size: 24px; }
  .letterhead .sender {
    position: absolute; left: 463px; top: 50px;
    font-size: 9.5px; line-height: 12.5px; color: var(--muted);
  }
  .sender .label { color: var(--brand-blue); }
  .letter-body {
    position: absolute; left: 93px; top: 245px; width: 452px;
    font-family: "Noto Sans", Arial, sans-serif;
    font-size: 9.6px; line-height: 11.6px; color: var(--ink); text-align: justify;
  }
  .letter-body p + p { margin-top: 12px; }
  .signature { position: absolute; left: 100px; top: 560px; width: 100px; height: 75px; background: #f2f2f2; }
  .letterhead .site-url {
    position: absolute; left: 75px; bottom: 8px; font-size: 9.5px; color: #fff;
  }

  /* Business card */
  .card-back { left: 758px; top: 83px; width: 252px; height: 144px;
    background: radial-gradient(circle at 30% 30%, var(--card-glow) 0%, #1a7ccc 35%, #1c5fb0 75%, #1f56a6 100%); }
  .card-back .wordmark { position: absolute; right: 26px; bottom: 14px; font-size: 14px; color: #fff; }
  .card-front { left: 758px; top: 232px; width: 252px; height: 144px; }
  .card-front .wordmark { position: absolute; left: 10px; top: 14px; font-size: 14px; }
  .card-front .holder { position: absolute; right: 16px; top: 56px; text-align: right; }
  .holder .name { font-size: 9px; color: var(--brand-blue); font-weight: 600; }
  .holder .role { font-size: 5.5px; color: var(--muted); }
  .card-front .contacts {
    position: absolute; left: 8px; top: 102px; list-style: none;
    font-size: 5.5px; line-height: 7.3px; color: #dfe8f6;
  }
  .contacts li { display: flex; align-items: center; gap: 4px; }
  .contacts svg { width: 5px; height: 5px; fill: #fff; }
  .card-front .card-address {
    position: absolute; right: 16px; top: 116px; text-align: right;
    font-size: 5.5px; line-height: 7.3px; color: #dfe8f6;
  }

  /* Compliment slip */
  .slip { left: 491px; top: 448px; width: 634px; height: 275px; box-shadow: 0 0 6px rgba(0,0,0,.5); }
  .slip .wordmark { position: absolute; left: 24px; top: 38px; font-size: 18px; }
  .slip .sender { position: absolute; left: 26px; top: 72px; font-size: 9.5px; line-height: 12.5px; color: var(--muted); }
  .slip .greeting {
    position: absolute; right: 26px; top: 192px;
    font-size: 20px; color: var(--brand-blue);
  }
</style>
</head>
<body>
  <svg width="0" height="0" style="position:absolute">
    <defs>
      <linearGradient id="band" x1="0" x2="1" y1="0" y2="0">
        <stop offset="0" stop-color="#2f74b8"/>
        <stop offset="1" stop-color="#2a3f99"/>
      </linearGradient>
    </defs>
  </svg>

  <article class="sheet letterhead">
    <div class="wordmark"><span>Larkfield Checks</span><span class="mark-dot"></span></div>
    <address class="sender" style="font-style:normal">
      418 Marden Row<br>
      Suite 12 Larkfield, KT 20931<br>
      <span class="label">Phone.</span> (555) 014-2290<br>
      <span class="label">Fax.</span> (555) 014-2290
    </address>
    <div class="letter-body">
      <p>In dui turpis, varius vitae, tincidunt id, consequat ut, leo. Donec tincidunt tristique odio. Nulla erat felis, euismod nec, fringilla non, aliquet et, magna. Nulla at magna quis nisi pretium vehicula. Pellentesque habitant morbi tristique senectus et netus et malesuada fames ac turpis egestas. Class aptent taciti sociosqu ad litora torquent per conubia nostra, per inceptos himenaeos. In vel quam. Phasellus varius convallis purus. In non turpis. Nam sed risus. Etiam non neque at nisl gravida porttitor. Donec leo dolor, feugiat ut, pharetra et, porttitor a, metus. Suspendisse laoreet magna vel elit. Ut est augue, fermentum ac, molestie at, vestibulum et, urna.</p>
      <p>Nunc purus. Cras auctor. In ornare neque id ipsum. Nulla tincidunt, diam sit amet viverra euismod, sapien augue fringilla neque, at pellentesque felis tortor vel enim. Etiam dignissim. Sed a tortor vel nisl euismod ultricies. Donec molestie congue lectus. Integer sed turpis a tortor imperdiet consequat. Maecenas molestie placerat urna. Sed pede enim, sollicitudin nec, pretium nec, sollicitudin a, felis. In hac habitasse platea dictumst. Nam facilisis, tellus non scelerisque placerat, turpis turpis semper ante, euismod imperdiet augue nisi et neque. Vivamus tincidunt.</p>
      <p>Nulla lobortis ultricies nulla. Pellentesque purus mi, consequat quis, hendrerit at, aliquam non, eros. Nullam urna est, vehicula nec, cursus nec, dignissim sit amet, lectus. Quisque tellus sit amet laoreet ullamcorper, urna nisi fringilla ante, at rhoncus justo ligula in nunc. Sed hendrerit luctus lorem. Aenean tempor, metus vel posuere gravida, arcu nunc vulputate leo, quis blandit sem magna a turpis. Vivamus in neque. Lorem ipsum dolor sit amet, consectetur adipiscing elit. Duis tristique tortor id nisl feugiat posuere. Maecenas posuere, velit eget tempor hendrerit. Praesent porta tempus ligula. Morbi in leo. Curabitur sapien metus, tincidunt sed, rhoncus in, porttitor et, odio. Praesent sed justo sed arcu commodo feugiat. Donec viverra lorem. Cras libero. Donec mollis consectetuer metus. Praesent odio.</p>
    </div>
    <div class="signature" role="img" aria-label="Handwritten signature of the sender"></div>
    <svg class="wave" viewBox="0 0 612 90" height="90" preserveAspectRatio="none" aria-hidden="true">
      <path d="M0 48 C160 38 300 90 612 22 L612 90 L0 90 Z" fill="url(#band)"/>
    </svg>
    <span class="site-url">www.larkfieldchecks.co.uk</span>
  </article>

  <section class="sheet card-back">
    <svg class="wave" viewBox="0 0 252 40" height="40" preserveAspectRatio="none" aria-hidden="true">
      <path d="M0 22 C80 8 150 40 252 18" fill="none" stroke="rgba(255,255,255,.25)" stroke-width="2"/>
      <path d="M0 30 C90 16 160 44 252 26" fill="none" stroke="rgba(255,255,255,.15)" stroke-width="2"/>
    </svg>
    <div class="wordmark"><span>Larkfield Checks</span><span class="mark-dot" style="width:5px;height:5px"></span></div>
  </section>

  <section class="sheet card-front">
    <div class="wordmark"><span>Larkfield Checks</span><span class="mark-dot" style="width:5px;height:5px"></span></div>
    <div class="holder">
      <div class="name">Dana Holloway</div>
      <div class="role">Managing Director</div>
    </div>
    <svg class="wave" viewBox="0 0 252 60" height="60" preserveAspectRatio="none" aria-hidden="true">
      <path d="M0 10 C70 0 120 40 252 4 L252 60 L0 60 Z" fill="url(#band)"/>
    </svg>
    <ul class="contacts">
      <li><svg viewBox="0 0 10 10"><path d="M2 1h2l1 2-1 1c1 2 2 3 3 3l1-1 2 1v2c-5 0-8-3-8-8z"/></svg>(555) 014-2200</li>
      <li><svg viewBox="0 0 10 10"><rect x="1" y="3" width="8" height="5"/></svg>(555) 014-2290</li>
      <li><svg viewBox="0 0 10 10"><path d="M1 2h8v6H1z"/></svg>dana@larkfieldchecks.co.uk</li>
      <li><svg viewBox="0 0 10 10"><circle cx="5" cy="5" r="4"/></svg>www.larkfieldchecks.co.uk</li>
    </ul>
    <div class="card-address">77 Orchard Loop<br>Larkfield, KT 20933</div>
  </section>

  <article class="sheet slip">
    <div class="wordmark"><span>Larkfield Checks</span><span class="mark-dot" style="width:6px;height:6px"></span></div>
    <address class="sender" style="font-style:normal">418 Marden Row<br>Suite 12 Larkfield, KT 20931</address>
    <p class="greeting">With Compliments</p>
    <svg class="wave" viewBox="0 0 634 60" height="60" preserveAspectRatio="none" aria-hidden="true">
      <path d="M0 12 C170 4 320 66 634 6 L634 60 L0 60 Z" fill="url(#band)"/>
    </svg>
  </article>
</body>
</html>
```